Logo & Visitenkarte für Personal Shopping
Zielgruppe
Ich biete Personal Shopping und suche ein stylisches Design, meine Zielgruppe sind Frauen und Männer im mittleren Alter.
Aufgabenstellung
Ich suche ein stylisches Design für Kunden, die Neugier auf Mode, Sinn für guten Stil, Lust auf Farbe und Mut zur Veränderung haben.

```html
<!DOCTYPE html>
<html lang="de">
<head>
<meta charset="utf-8">
<title>Henrik Valdt – Personal Shopping Visitenkarte</title>
<link href="https://fonts.googleapis.com/css2?family=Montserrat:wght@400;500&display=swap" rel="stylesheet">
<style>
  :root {
    --backdrop: #2c2c2c;
    --card-dark: #454545;
    --card-light: #ffffff;
    --accent: #b85f25;
    --text-light: #ffffff;
    --text-dark: #3f3f3f;
  }
  * { margin: 0; padding: 0; box-sizing: border-box; }
  html, body { width: 1200px; height: 780px; overflow: hidden; }
  body {
    background: var(--backdrop);
    font-family: "Montserrat", Arial, sans-serif;
    position: relative;
  }
  .card {
    position: absolute;
    top: 195px;
    width: 254px;
    height: 396px;
    overflow: hidden;
  }
  .card--front { left: 314px; background: var(--card-dark); }
  .card--back { left: 639px; background: var(--card-light); }

  .accent-band {
    position: absolute;
    left: 0; width: 100%;
    height: 16px;
    background: var(--accent);
  }
  .card--front .accent-band { bottom: 0; }
  .card--back .accent-band { top: 245px; }

  .brand {
    position: absolute;
    left: 0; width: 100%;
    text-align: center;
  }
  .brand__name {
    font-weight: 500;
    white-space: nowrap;
    line-height: 1;
  }
  .brand__tagline {
    color: var(--accent);
    font-weight: 400;
    letter-spacing: 0.06em;
    line-height: 1;
  }
  .card--front .brand { top: 199px; }
  .card--front .brand__name { color: var(--text-light); font-size: 24px; }
  .card--front .brand__tagline { font-size: 8px; margin-top: 8px; }

  .card--back .brand { top: 127px; }
  .card--back .brand__name { color: var(--text-dark); font-size: 21px; }
  .card--back .brand__tagline { font-size: 7px; margin-top: 7px; }

  .contact {
    position: absolute;
    left: 0; top: 261px;
    width: 100%; height: 135px;
    background: var(--card-dark);
    color: var(--text-light);
    text-align: center;
    font-size: 9px;
    line-height: 13px;
    font-style: normal;
    padding-top: 18px;
  }
  .contact__social { font-size: 8px; margin-top: 1px; }
  .contact__reach { margin-top: 21px; }
</style>
</head>
<body>
  <section class="card card--front" aria-label="Vorderseite">
    <div class="brand">
      <p class="brand__name">Henrik Valdt</p>
      <p class="brand__tagline">Personal Shopping</p>
    </div>
    <div class="accent-band"></div>
  </section>

  <section class="card card--back" aria-label="Rückseite">
    <div class="brand">
      <p class="brand__name">Henrik Valdt</p>
      <p class="brand__tagline">Personal Shopping</p>
    </div>
    <div class="accent-band"></div>
    <address class="contact">
      <p>Lindenweg 12</p>
      <p>54321 Musterfeld</p>
      <p class="contact__social">@henrikvaldt</p>
      <div class="contact__reach">
        <p>+49 151 23456789</p>
        <p>info@henrikvaldt.de</p>
        <p>www.henrikvaldt.de</p>
      </div>
    </address>
  </section>
</body>
</html>
```